Junior Rugby Event needs 4 page Brochure

4 Page A4 brochure to be designed for a junior rugby event to be held in japan.. The brochure will entice coaches, teachers and players to the event.
The brochure will provide a basic overview of the event - dates, venue and promote some of the key features of the host, venue and event.
Event logo has been included. Design overview with copy has been included as word document. Images have been attached that can be used or alternatives sourced. A PDF document has been included of a design example that we like.
Target Market(s)
Rugby Clubs and Schools
Industry/Entity Type
Events
Look and feel

```html
<!DOCTYPE html>
<html lang="en">
<head>
<meta charset="utf-8">
<title>Pacific Youth Rugby Festival – Brochure</title>
<link rel="stylesheet" href="https://fonts.googleapis.com/css2?family=Oswald:wght@400;500&family=Open+Sans:wght@400;600;700&family=Dancing+Script:wght@600&display=swap">
<style>
:root{
  --red:#b81c22;
  --navy:#1d2556;
  --white:#ffffff;
  --paper:#f4f4f4;
  --ink:#3a3a3a;
  --backdrop:#d6d7d9;
  --photo-green:#6d8f4a;
  --photo-dark:#2f3a2a;
}
*{margin:0;padding:0;box-sizing:border-box}
html,body{width:920px;height:1200px;overflow:hidden;background:var(--backdrop)}
body{position:relative;font-family:"Open Sans",sans-serif;color:var(--ink)}
.spread{position:absolute;left:100px;width:718px;display:flex}
.spread--outer{top:72px;height:508px}
.spread--inner{top:634px;height:498px}
.page{position:relative;width:359px;height:100%;background:var(--white);overflow:hidden}
.heading{font-family:"Oswald",sans-serif;font-weight:400;line-height:1}
.body-copy{font-size:7px;line-height:9.6px}
.abs{position:absolute}
.photo{position:absolute}

/* back page */
.tab{position:absolute;left:0;top:28px;height:21px;width:153px;background:var(--red);color:var(--white);
  font-size:11.5px;padding:4px 0 0 18px;clip-path:polygon(0 0,95% 0,100% 100%,0 100%)}
.intro{left:18px;top:66px;width:322px}
.package{position:absolute;left:18px;width:320px;border:1px solid var(--red);padding:14px 10px 0 9px}
.package__title{position:absolute;left:3px;top:-8px;background:var(--white);padding:0 5px 0 0;color:var(--navy);font-size:11.5px}
.package ul{list-style:none;font-size:6.8px;line-height:11.6px}
.package li::before{content:"• "}
.contact{left:16px;top:435px;width:210px;color:var(--white);font-size:8.4px;line-height:12.8px}
.contact strong{font-weight:700}
.event-name{font-family:"Oswald",sans-serif;font-weight:500;text-transform:uppercase;text-align:center;line-height:1.05}
.event-name--small{left:252px;top:418px;width:104px;color:var(--navy);font-size:13px}
.event-name--large{left:214px;top:80px;width:132px;color:var(--white);font-size:17px}
.dot{display:block;width:12px;height:12px;border-radius:50%;margin:0 auto 5px}

/* cover */
.cover-title{position:absolute;left:0;top:378px;width:354px;height:80px;background:var(--red);color:var(--white);
  padding:10px 0 0 16px;clip-path:polygon(0 0,100% 0,88% 100%,0 100%)}
.cover-title h1{font-size:23px;letter-spacing:-.2px}
.cover-title p{font-size:12.2px;line-height:15px;margin-top:7px}
.website{left:0;top:478px;width:359px;text-align:center;color:var(--navy);font-size:13.5px;letter-spacing:1.2px}

/* inner */
.overview-band{position:absolute;left:0;top:0;width:359px;height:152px;background:var(--red)}
.overview{left:17px;top:20px;width:210px;color:var(--white)}
.overview h2{font-size:14px;margin-bottom:6px}
.overview p{font-size:6.8px;line-height:9.5px;margin-bottom:8px;text-align:justify}
.story{left:17px;width:330px;text-align:justify}
.signature{left:17px;top:224px;display:flex;align-items:baseline;gap:28px}
.signature__name{font-family:"Dancing Script",cursive;font-size:13px;color:#222}
.signature__role{font-size:6.8px;font-style:italic;text-transform:uppercase}
.label{color:var(--red);font-size:7.6px;font-weight:600}
.label::before{content:"";display:inline-block;border-left:5px solid var(--red);border-top:3.5px solid transparent;border-bottom:3.5px solid transparent;margin-right:5px}
.facts{left:16px;width:330px;text-align:justify}
.strip{position:absolute;top:45px;height:80px}
</style>
</head>
<body>

<section class="spread spread--outer">
  <article class="page page--back">
    <div class="tab heading">Travel &amp; Tournament Package</div>
    <p class="abs body-copy intro">Our aim is to make participation in the Pacific Youth Rugby Festival as simple as possible for you, we therefore a number of different tournament packages. We also have a network of agents around the world who will assist you with flights and tour extension options.</p>

    <div class="package" style="top:122px;height:98px">
      <h3 class="package__title heading">Seaside Arena Player Package</h3>
      <ul>
        <li>6 nights accommodation in Seaside Arena Lodges, bunk rooms.</li>
        <li>Breakfast, Lunch and Dinner each day</li>
        <li>Airport or Train Station Transfers - one per team for arrival and departure.</li>
        <li>Tournament Entry (4 games guaranteed)</li>
        <li>Half Day Guided Fukuoka Sightseeing Tour including Kushida Shrine and Fukuoka Castle</li>
        <li>Exclusive Pacific Youth Rugby Festival Merchandise</li>
      </ul>
    </div>

    <div class="package" style="top:245px;height:105px">
      <h3 class="package__title heading">Fukuoka Player or Supporter Package</h3>
      <ul>
        <li>6 nights hotel accommodation in Fukuoka City.</li>
        <li>Breakfast daily</li>
        <li>Airport or Train Station Transfers - one per team for arrival and departure.</li>
        <li>Tournament Return Shuttle Service</li>
        <li>Tournament Entry (4 games guaranteed)</li>
        <li>Half Day Guided Fukuoka Sightseeing Tour including Kushida Shrine and Fukuoka Castle</li>
        <li>Exclusive Pacific Youth Rugby Festival Merchandise</li>
      </ul>
    </div>

    <svg class="abs" style="left:0;top:320px" width="359" height="188" viewBox="0 0 359 188" aria-hidden="true">
      <polygon points="0,0 190,112 0,30" fill="var(--navy)"/>
      <polygon points="0,30 190,112 284,188 0,188" fill="var(--red)"/>
    </svg>

    <p class="abs contact">Please contact us to<br>receive a tailored quote<br>for your team for the<br>Pacific Youth Rugby<br><strong>hello@pacificyouthrugbyfest.com</strong></p>

    <div class="abs event-name event-name--small"><span class="dot" style="background:var(--red)"></span>Pacific Youth<br>Rugby Festival<br>Japan 2019</div>
  </article>

  <article class="page page--cover">
    <div class="photo" role="img" aria-label="Junior rugby players running with the ball in front of a stadium stand"
         style="left:17px;top:14px;width:335px;height:456px;background:linear-gradient(180deg,#b9a66a 0%,#c9534a 18%,#8a9f6a 40%,var(--photo-green) 100%)"></div>
    <svg class="abs" style="left:0;top:0" width="359" height="470" viewBox="0 0 359 470" aria-hidden="true">
      <polygon points="128,0 359,0 359,260" fill="var(--navy)"/>
      <polygon points="359,170 359,470 190,470" fill="var(--red)"/>
    </svg>
    <div class="abs event-name event-name--large"><span class="dot" style="background:var(--white)"></span>Pacific Youth<br>Rugby Festival<br>Japan 2019</div>

    <div class="cover-title">
      <h1 class="heading">2019 Pacific Youth Rugby Festival</h1>
      <p>Fukuoka, Japan<br>30th September to 4th October 2019</p>
    </div>
    <p class="abs website">www.pacificyouthrugbyfest.com</p>
  </article>
</section>

<section class="spread spread--inner">
  <article class="page page--overview">
    <div class="overview-band"></div>
    <div class="photo" role="img" aria-label="Young players contesting a tackle on the pitch"
         style="left:230px;top:0;width:129px;height:152px;background:linear-gradient(160deg,#3f5a2e,#7ea257);clip-path:polygon(28px 0,100% 0,100% 100%,10px 100%)"></div>
    <svg class="abs" style="left:0;top:0" width="359" height="152" viewBox="0 0 359 152" aria-hidden="true">
      <polygon points="248,0 258,0 240,152 228,152" fill="var(--navy)"/>
    </svg>
    <div class="abs overview">
      <h2 class="heading">Tournament Overview</h2>
      <p>The Pacific Youth Rugby Festival has been created to provide a meeting point for young rugby players from across the globe as the eyes of the rugby world turn towards Japan in 2019. This event will provide a once in a lifetime experience, both on and off the field.</p>
      <p>Teams will have the opportunity to match up against international opponents and as well as taking in some of the unique culture and history of Japan. Teams will be guaranteed 4 games during the event.</p>
    </div>

    <p class="abs body-copy story" style="top:165px">The tournament will feature school, club and development teams from across the Rugby World. Invitations have been sent to teams across the rugby world to Australia, New Zealand, England, Ireland, Scotland, Wales, South Africa, USA, Canada, Argentina, France, Asia and the Pacific Islands.</p>
    <p class="abs body-copy story" style="top:204px">We invite you to join us in Japan for this celebration of rugby.</p>
    <div class="abs signature"><span class="signature__name">Daniel Harper</span><span class="signature__role">Chairman – Pacific Youth Rugby Festival</span></div>

    <p class="abs label" style="left:17px;top:245px">Venue</p>
    <p class="abs body-copy story" style="top:257px">The Seaside Sports Arena is a multi purpose sports venue with 5 football fields , track and field facilities, multiple tennis courts, gymnasium, martial arts dojo, training center, conference center, restaurants and accommodation. with the main stadium seating 10,000 spectators and is the home ground of the Fukuoka Harbour Blues.</p>
    <p class="abs body-copy story" style="top:307px">In addition to the fantastic sports facilities the Seaside Sports Arena has onsite accommodation in Lodges and onsite dining options including Cafeteria with seating for up to 250, Buffet Restaurant, Traditional Japanese Restaurant, Bakery and Cafe as well BBQ areas.</p>

    <div class="photo" role="img" aria-label="Rugby ball resting on the grass of a training pitch"
         style="left:0;top:344px;width:359px;height:142px;background:linear-gradient(180deg,#4a3a2c 0%,#5d7a3a 45%,var(--photo-dark) 100%)"></div>
  </article>

  <article class="page page--host">
    <div class="overview-band"></div>
    <div class="strip" role="img" aria-label="Red shrine gate in Fukuoka" style="left:2px;width:122px;background:linear-gradient(180deg,#9fc3e4,#c94a36);clip-path:polygon(0 0,100% 0,95% 100%,0 100%)"></div>
    <div class="strip" role="img" aria-label="Rugby balls lined up on a field" style="left:122px;width:124px;background:linear-gradient(180deg,#3c4a33,#5e7a3c);clip-path:polygon(5% 0,100% 0,95% 100%,0 100%)"></div>
    <div class="strip" role="img" aria-label="Neon-lit city street at night" style="left:244px;width:115px;background:linear-gradient(180deg,#1a1a3a,#c2463e 60%,#e0b040);clip-path:polygon(5% 0,100% 0,100% 100%,0 100%)"></div>

    <p class="abs label" style="left:16px;top:163px">Where</p>
    <p class="abs body-copy facts" style="top:175px">Fukuoka is the largest city on the island of Kyushu, the third largest of Japan's islands, and the sixth largest city in Japan with a population in excess of 2.5 million.</p>
    <p class="abs body-copy facts" style="top:203px">As a major regional hub Fukuoka has direct flight connections from Tokyo, Osaka, Shanghai, Seoul, Bangkok, Singapore, Tapai, Hoi Chi Minh, Hong Kong and Honolulu, as well as via Shinkansen to the rest of Japan including Tokyo, Hiroshima, Kyoto and Osaka.</p>
    <p class="abs body-copy facts" style="top:242px">Fukuoka City is home to one of the 2019 Global Rugby Cup Venues, Hakata Forest Stadium with a capacity of 22,563 built in 1995. Hakata Forest Stadium will host three Cup fixtures including France versus USA on Wednesday 2nd October 2019.</p>

    <p class="abs label" style="left:16px;top:290px">Who</p>
    <p class="abs body-copy facts" style="top:302px">The Tournament will feature U17, U15 &amp; U13 Categories and is open to club, school and development teams. Each age category will be seeded with the ability to play off for Plate, Bowl and Trophy divisions.</p>

    <div class="photo" role="img" aria-label="Team in light blue kit gathered in a huddle before a match"
         style="left:0;top:344px;width:359px;height:142px;background:linear-gradient(180deg,#c9ccd6 0%,#8fa9c8 40%,#2b3550 80%,#4f7a3a 100%)"></div>
  </article>
</section>

</body>
</html>
```